KEP Business Card

the business card should be double sided.
Will need to be Korean on one side and english on the other.
it will need to have:

address
website
skype
phone
cell
fax
name
title
email

just put in dummy details to start - i will then give you correct info once we have the format right.

Also - if you feel creative about the logo we are happy to make some amendments to it so it looks right. We are still at early stages with the logo so happy if you have suggestions around the logo concept.
Updates

The deadline for this has been brought forward to Wednesday 11th December. We can not review any designs after this date.

we will need to make a decision by Wednesday 11th December, so please have designs in by this date and not by the deadline set by lumahive

Target Market(s)

large companies, executives

Industry/Entity Type

Business

Colors

Designer to choose colors to be used in the design.

Requirements
Must have
• double sided - english on one side and korean on the other. we will give you korean wording once we have a design we like.

```html
<!DOCTYPE html>
<html lang="en">
<head>
<meta charset="utf-8">
<title>KEP Business Card</title>
<link href="https://fonts.googleapis.com/css2?family=Open+Sans:wght@400;600&display=swap" rel="stylesheet">
<style>
  :root {
    --kep-blue: #2b4f96;
    --kep-blue-light: #4a6db3;
    --card-white: #ffffff;
    --stage: #eceef2;
    --ink-soft: #3a4f7e;
  }
  * { margin: 0; padding: 0; box-sizing: border-box; }
  html, body { width: 1200px; height: 981px; overflow: hidden; }
  body {
    background: var(--stage);
    font-family: "Open Sans", Arial, sans-serif;
    display: flex;
    flex-direction: column;
    align-items: center;
    justify-content: center;
    gap: 50px;
  }
  .card {
    position: relative;
    width: 700px;
    height: 400px;
    border-radius: 22px;
    overflow: hidden;
    box-shadow: 0 6px 18px rgba(30, 45, 80, 0.18);
  }
  /* Back side */
  .card-back {
    background: var(--kep-blue);
    color: var(--card-white);
    display: flex;
    flex-direction: column;
    align-items: center;
    justify-content: center;
  }
  .brand-name {
    font-weight: 600;
    font-size: 44px;
    letter-spacing: 3px;
    line-height: 1;
  }
  .card-back .brand-name { margin-top: 10px; }
  .card-back .website {
    margin-top: 60px;
    font-size: 15px;
    letter-spacing: 2.5px;
    opacity: 0.9;
  }
  /* Front side */
  .card-front { background: var(--card-white); }
  .card-front .wave { position: absolute; inset: 0; }
  .contact-list {
    position: absolute;
    left: 58px;
    top: 44px;
    list-style: none;
    color: var(--ink-soft);
    font-size: 13px;
    line-height: 1;
  }
  .contact-list li {
    display: flex;
    align-items: center;
    gap: 10px;
    height: 23px;
  }
  .contact-icon {
    width: 13px; height: 13px;
    border-radius: 50%;
    background: var(--kep-blue);
    flex: none;
  }
  .card-front .brand-name {
    position: absolute;
    right: 70px;
    top: 155px;
    color: var(--kep-blue);
  }
  .holder {
    position: absolute;
    right: 48px;
    bottom: 30px;
    text-align: right;
    color: var(--card-white);
  }
  .holder-name { font-size: 22px; font-weight: 600; }
  .holder-title { font-size: 16px; margin-top: 2px; }
</style>
</head>
<body>
  <section class="card card-back">
    <div class="brand-name">KEP</div>
    <div class="website">www.kepsample.com</div>
  </section>

  <section class="card card-front">
    <svg class="wave" viewBox="0 0 700 400" preserveAspectRatio="none" aria-hidden="true">
      <path d="M0,170 C90,300 330,300 700,290 L700,400 L0,400 Z" fill="var(--kep-blue-light)"/>
      <path d="M0,195 C100,330 360,320 700,305 L700,400 L0,400 Z" fill="var(--kep-blue)"/>
      <path d="M0,215 C120,320 380,305 700,300" fill="none" stroke="var(--card-white)" stroke-width="3"/>
    </svg>
    <ul class="contact-list">
      <li><span class="contact-icon"></span>Suite # 410, Oak Bldg.</li>
      <li><span class="contact-icon" style="visibility:hidden"></span>NY 10234</li>
      <li><span class="contact-icon"></span>555-014-2210</li>
      <li><span class="contact-icon"></span>555-017-8841</li>
      <li><span class="contact-icon"></span>555-019-3376</li>
      <li><span class="contact-icon"></span>name@kepsample.com</li>
      <li><span class="contact-icon"></span>www.kepsample.com</li>
    </ul>
    <div class="brand-name">KEP</div>
    <div class="holder">
      <div class="holder-name">Daniel Reyes</div>
      <div class="holder-title">Owner / C.E.O</div>
    </div>
  </section>
</body>
</html>
```